Your complete Gardening and lawn maintenance, Horticultural care. (to be on card)
We are looking at using a logo of a tree, with a recycling emblem circling the tree. The colors of choice, are burnt oranges and olive greens. Presented; simple to the eye, yet catchy to the clients in a eco-friendly way. We have uploaded a design for you to look at just to give a rough idea, you can use that or create your own ideas or play around with a mixture.

Target Market(s)

Home owners, businesses, real estates.

Industry/Entity Type

Recycling

Contact Information for Business Card

Name: Colin Breversted
Phone: 0438159027
Email: brightmossyards@mailbarn.net

Logo Text

Bright-Moss Yards

Logo styles of interest
Emblem Logo
Pictorial/Combination Logo
Abstract Logo
Requirements
Must have
• Business name: Bright-Moss Yards
and slogan : Your complete Gardening and lawn maintenance, Horticultural care

```html
<!DOCTYPE html>
<html lang="en">
<head>
<meta charset="utf-8">
<title>Bright-Moss Yards – Business Card</title>
<link rel="stylesheet" href="https://fonts.googleapis.com/css2?family=Poppins:wght@600&family=Crimson+Text:ital,wght@0,400;0,600;1,400&display=swap">
<style>
  :root {
    --band: #74766a;
    --leaf: #7dcb6a;
    --leaf-soft: #a9d86e;
    --white: #ffffff;
    --ink: #1c1a1a;
  }
  html, body {
    margin: 0;
    padding: 0;
    overflow: hidden;
    background: var(--white);
  }
  .card {
    position: relative;
    width: 1200px;
    height: 693px;
    overflow: hidden;
    background: var(--white);
  }
  .header-band {
    position: absolute;
    left: 0;
    top: 0;
    width: 1200px;
    height: 371px;
    background: var(--band);
  }
  .brand-name {
    position: absolute;
    left: 131px;
    top: 188px;
    margin: 0;
    font-family: "Poppins", sans-serif;
    font-weight: 600;
    font-size: 98px;
    line-height: 1;
    letter-spacing: -1px;
    white-space: nowrap;
    color: var(--white);
  }
  .brand-name .accent { color: var(--leaf); }
  .tagline {
    position: absolute;
    left: 105px;
    top: 302px;
    margin: 0;
    font-family: "Crimson Text", serif;
    font-size: 34px;
    line-height: 1;
    letter-spacing: -0.6px;
    white-space: nowrap;
    color: var(--white);
  }
  .mark {
    position: absolute;
    left: 164px;
    top: 398px;
    width: 176px;
    height: 180px;
    display: flex;
    flex-direction: column;
    align-items: center;
    justify-content: center;
    gap: 10px;
  }
  .mark-dot {
    width: 110px;
    height: 110px;
    border-radius: 50%;
    background: var(--leaf-soft);
  }
  .mark-name {
    font-family: "Crimson Text", serif;
    font-weight: 600;
    font-size: 20px;
    color: var(--ink);
    white-space: nowrap;
  }
  .contact {
    position: absolute;
    left: 376px;
    top: 418px;
    font-family: "Crimson Text", serif;
    color: var(--ink);
  }
  .contact-name {
    margin: 0 0 10px;
    font-weight: 400;
    font-size: 48px;
    line-height: 1;
    font-variant: small-caps;
    letter-spacing: 2px;
  }
  .contact-email {
    margin: 0 0 6px;
    font-style: italic;
    font-size: 33px;
    line-height: 1.15;
  }
  .contact-phone {
    margin: 0;
    font-size: 35px;
    line-height: 1.15;
  }
</style>
</head>
<body>
  <main class="card">
    <div class="header-band"></div>
    <h1 class="brand-name"><span class="accent">Bright-Moss</span> Yards</h1>
    <p class="tagline">Your complete Gardening and lawn maintenance, Horticultural care</p>

    <div class="mark">
      <div class="mark-dot"></div>
      <span class="mark-name">Bright-Moss Yards</span>
    </div>

    <section class="contact">
      <h2 class="contact-name">Colin Breversted</h2>
      <p class="contact-email">brightmossyards@mailbarn.net</p>
      <p class="contact-phone">Phone: 0438159027</p>
    </section>
  </main>
</body>
</html>
```